Design some Business Cards for Varnok Advisory

A new business card design - scope

2 sides
Side 1 - varnok logo & add what you think might be good
Side 2 - name address etc & varnok logo. Use logos for twitter if you want

Name - Gideon Marsh
Position - Managing Director
Address - Level 5, 27 Harrow Lane, Melbourne, VIC 3000
Tel - +61 3 9555 0187
Mob - +61 491 570 236
Email - gmarsh@varnok.com.au
Web - www.varnok.com.au
Twitter - talkline.example/varnokadvise
LinkedIn - proflink.example/gideon

Font for name etc - Rockwell

Colours

Blue -Cyan 96%, Magenta 66%, Yellow 8%, Black 30%

Grey - Cyan 55%, Magenta 46%, Yellow 42%, Black 2%

Current card is Varnok Biz card Front & Back v2.0

Logos are attached - up to you to use blue or white varnok logo.

```html
<!DOCTYPE html>
<html lang="en">
<head>
<meta charset="utf-8">
<title>Varnok Advisory – Business Cards</title>
<link rel="stylesheet" href="https://fonts.googleapis.com/css2?family=Open+Sans:wght@400;700&family=Raleway:wght@300&display=swap">
<style>
  :root {
    --brand-blue: #1f4a9e;
    --brand-blue-deep: #17397c;
    --brand-grey: #708791;
    --swoosh-dark: #2b2b2e;
    --card-white: #ffffff;
    --card-shade: #eceef1;
    --ink: #2a2f38;
    --rule: #c9ccd2;
    --stage: #e6e7ea;
  }
  html, body {
    margin: 0;
    width: 1200px;
    height: 901px;
    overflow: hidden;
    background: var(--stage);
  }
  .sheet {
    width: 1200px;
    height: 901px;
    display: flex;
    align-items: center;
    justify-content: center;
    gap: 40px;
  }
  .card {
    position: relative;
    width: 540px;
    height: 330px;
    border-radius: 22px;
    overflow: hidden;
    box-shadow: 0 6px 18px rgba(0,0,0,0.18);
  }
  .card--front {
    background: linear-gradient(160deg, var(--card-white) 0%, var(--card-shade) 100%);
  }
  .card--back {
    background: radial-gradient(ellipse at 40% 35%, #2c5bb3 0%, var(--brand-blue) 55%, var(--brand-blue-deep) 100%);
  }
  .card__band {
    position: absolute;
    inset: 0;
    width: 540px;
    height: 330px;
  }
  .brand {
    position: absolute;
    margin: 0;
    font-family: "Raleway", sans-serif;
    font-weight: 300;
    text-transform: uppercase;
    letter-spacing: 0.22em;
    white-space: nowrap;
  }
  .card--front .brand {
    top: 54px;
    left: 168px;
    font-size: 26px;
    color: var(--brand-blue);
  }
  .card--back .brand {
    top: 138px;
    left: 0;
    right: 0;
    text-align: center;
    font-size: 34px;
    color: var(--card-white);
  }
  .address {
    position: absolute;
    top: 110px;
    left: 290px;
    margin: 0;
    font-family: "Open Sans", sans-serif;
    font-style: normal;
    font-size: 12px;
    line-height: 1.45;
    color: var(--ink);
  }
  .person {
    position: absolute;
    left: 34px;
    top: 138px;
    font-family: "Open Sans", sans-serif;
  }
  .person__name {
    margin: 0;
    font-size: 17px;
    font-weight: 700;
    color: var(--brand-blue);
  }
  .person__role {
    margin: 0 0 8px;
    padding-bottom: 6px;
    width: 190px;
    font-size: 12px;
    color: var(--ink);
    border-bottom: 1px solid var(--rule);
  }
  .contacts {
    list-style: none;
    margin: 0;
    padding: 0;
    font-size: 11px;
    line-height: 19px;
    color: var(--ink);
  }
  .contacts li {
    display: flex;
    align-items: center;
    gap: 8px;
    white-space: nowrap;
  }
  .contacts svg {
    width: 11px;
    height: 11px;
    flex: none;
  }
  .back__web {
    position: absolute;
    left: 30px;
    bottom: 26px;
    margin: 0;
    font-family: "Open Sans", sans-serif;
    font-size: 11px;
    color: rgba(255,255,255,0.8);
  }
</style>
</head>
<body>
<main class="sheet">

  <section class="card card--front" aria-label="Card front with contact details">
    <svg class="card__band" viewBox="0 0 540 330" aria-hidden="true">
      <path d="M250 330 C 360 300, 470 230, 540 150 L540 330 Z" fill="var(--brand-blue)"/>
      <path d="M230 330 C 350 296, 460 222, 540 138 L540 150 C 470 230, 360 300, 250 330 Z" fill="var(--swoosh-dark)"/>
      <path d="M214 330 C 340 292, 452 216, 540 126 L540 130 C 454 220, 342 296, 222 330 Z" fill="var(--brand-grey)" opacity="0.6"/>
    </svg>

    <p class="brand">Varnok Advisory</p>

    <address class="address">Level 5, 27 Harrow Lane,<br>Melbourne, VIC 3000</address>

    <div class="person">
      <h1 class="person__name">Gideon Marsh</h1>
      <p class="person__role">Managing Director</p>
      <ul class="contacts">
        <li>
          <svg viewBox="0 0 12 12"><path d="M3 1 L5 3.5 L4 5 C4.8 6.6 5.6 7.4 7 8 L8.5 7 L11 9 L9.6 11 C5.5 10.6 1.4 6.5 1 2.4 Z" fill="var(--brand-blue)"/></svg>
          +61 3 9555 0187
        </li>
        <li>
          <svg viewBox="0 0 12 12"><rect x="3" y="0.5" width="6" height="11" rx="1" fill="none" stroke="var(--brand-blue)" stroke-width="1.3"/><circle cx="6" cy="9.4" r="0.8" fill="var(--brand-blue)"/></svg>
          +61 491 570 236
        </li>
        <li>
          <svg viewBox="0 0 12 12"><circle cx="6" cy="6" r="5" fill="none" stroke="var(--brand-blue)" stroke-width="1.3"/><path d="M1 6 H11 M6 1 C3.5 4 3.5 8 6 11 M6 1 C8.5 4 8.5 8 6 11" fill="none" stroke="var(--brand-blue)" stroke-width="0.9"/></svg>
          www.varnok.com.au
        </li>
        <li>
          <svg viewBox="0 0 12 12"><rect x="0.5" y="2.5" width="11" height="7.5" fill="none" stroke="var(--brand-blue)" stroke-width="1.2"/><path d="M0.8 2.8 L6 6.8 L11.2 2.8" fill="none" stroke="var(--brand-blue)" stroke-width="1.1"/></svg>
          gmarsh@varnok.com.au
        </li>
        <li>
          <svg viewBox="0 0 12 12"><rect x="0.5" y="0.5" width="11" height="11" rx="1.5" fill="var(--brand-blue)"/></svg>
          proflink.example/gideon
        </li>
        <li>
          <svg viewBox="0 0 12 12"><rect x="0.5" y="0.5" width="11" height="11" rx="1.5" fill="var(--brand-blue)"/></svg>
          talkline.example/varnokadvise
        </li>
      </ul>
    </div>
  </section>

  <section class="card card--back" aria-label="Card back with brand name">
    <p class="brand">Varnok Advisory</p>
    <p class="back__web">www.varnok.com.au</p>
  </section>

</main>
</body>
</html>
```